website refresh/redesign needed for Printing e commerce website

We'd like a website refresh/redesign done with the specific goal of having the site act as a more effective funnel for leads.<br/><br/>We think that the current design is outdated.<br/><br/>We want our customers and partners to still recognize the website, Is a big chunk of our business is repeat orders. <br/>so it should not be a full redesign. General color scheme and such should remain the same so that it is clear we are the same company. <br/><br/>However, the updated website design should look more polished and convey high-quality products and services that we provide. <br/><br/>Our website is https://shopledgerformsnet.quillpaperdepot.com/ if you want to take a look at our current website design. <br/><br/>we need 3 pages redesigned... <br/><br/>1. homepage:https://shopledgerformsnet.quillpaperdepot.com/<br/><br/>2. Category page: <br/>https://shopledgerformsnet.quillpaperdepot.com/order-computer-checks-c-4.html<br/><br/>3. Product detail page: https://shopledgerformsnet.quillpaperdepot.com/voucher-computer-checks-p-35.html<br/><br/> I can provide many more pictures of our products if needed.<br/><br/><br/>BTW. I have another project here on brief bazaar, you can check the other ones too, so to make it easier to do both when working on this.<br/><br/> Please reach out to me should you have any questions or comments.

```html
<!DOCTYPE html>
<html lang="en">
<head>
<meta charset="utf-8">
<title>ShopLedgerForms – Business Checks</title>
<link rel="stylesheet" href="https://fonts.googleapis.com/css2?family=Open+Sans:wght@400;600;700;800&family=Raleway:wght@300;400&display=swap">
<style>
:root{
  --green-dark:#1e6a18;
  --green:#2f8a22;
  --green-bright:#46a632;
  --green-band:#3c8f2b;
  --ink:#333;
  --muted:#777;
  --line:#dcdcdc;
  --page:#ffffff;
  --hero:#efefef;
  --footer:#f2f2f2;
  --red:#c8321f;
  --check-pink:#e9b7cf;
  --check-green:#b4dbb9;
  --check-blue:#b3c9ea;
  --check-lilac:#d2c3ea;
}
*{box-sizing:border-box;margin:0;padding:0}
html,body{width:1200px;height:2384px;overflow:hidden}
body{font-family:"Open Sans",Arial,sans-serif;color:var(--ink);background:var(--page);position:relative}
.topbar{height:32px;background:var(--green-dark);color:#dfe;font-size:11px;display:flex;align-items:center;justify-content:space-between;padding:0 170px}
.header{height:48px;background:var(--green-dark);display:flex;align-items:center;padding:0 170px;gap:30px;border-top:1px solid rgba(255,255,255,.1)}
.brand{display:flex;align-items:center;gap:8px;color:#fff;font-weight:700;font-size:18px;width:220px;white-space:nowrap}
.brand-mark{width:18px;height:18px;background:#fff;border-radius:50%;flex:none}
.search{flex:0 0 420px;height:30px;background:#fff;display:flex}
.search input{flex:1;border:0;padding:0 10px;font:12px "Open Sans",sans-serif;color:#999}
.search button{width:40px;border:0;background:var(--green-bright);display:flex;align-items:center;justify-content:center}
.shipping{margin-left:auto;color:#fff;font-weight:700;font-size:19px;display:flex;align-items:center;gap:10px;white-space:nowrap}
.nav{height:32px;background:var(--green);display:flex;padding:0 170px;gap:34px;align-items:center}
.nav a{color:#fff;font-size:12px;font-weight:600;text-decoration:none}
.hero{height:448px;background:var(--hero);display:flex;justify-content:center;gap:60px;padding-top:36px}
.hero-col{width:400px}
.hero-col h2{font-size:36px;font-weight:600;color:var(--green-bright)}
.hero-col ul{list-style:none;font-size:12px;color:#666;margin:8px 0 16px}
.hero-col li::before{content:"• ";color:var(--green-bright)}
.hero-btn{display:inline-block;background:var(--green-bright);color:#fff;font-size:11px;padding:4px 12px}
.check-art{height:236px;margin-top:18px;border:1px solid #d8d8d8}
.check-art.computer{background:linear-gradient(160deg,var(--check-pink) 0%,#f6e3ec 30%,var(--check-green) 55%,#e6f3e7 75%,var(--check-blue) 100%)}
.check-art.manual{background:linear-gradient(160deg,var(--check-lilac) 0%,#eef0f8 30%,var(--check-blue) 55%,#e8eef8 75%,var(--check-green) 100%)}
.categories{display:flex;justify-content:center;gap:20px;margin-top:32px}
.card{width:210px;height:240px;border:1px solid var(--line);padding:10px;font-size:10px;color:#666}
.card h3{font-size:12px;color:var(--ink);font-weight:700;margin-bottom:6px}
.card-img{height:110px;margin-bottom:8px}
.card .tag{color:var(--red);font-weight:600}
.card .price{margin-top:8px;color:var(--green);font-weight:700}
.section-title{font-size:26px;font-weight:700;color:var(--ink);padding-left:170px;margin-top:30px}
.section-title span{color:var(--green-bright)}
.section-title::after{content:"";display:block;width:60px;height:3px;background:var(--green-bright);margin-top:6px}
.row{display:flex;gap:17px;padding-left:170px;margin-top:22px}
.layout-ico{width:80px;height:64px;border:1px solid var(--line);display:flex;flex-direction:column;justify-content:center;gap:4px;padding:10px}
.layout-ico i{display:block;height:10px;background:#8cc5e9}
.layout-ico i.alt{background:#dfeef8}
.soft{width:80px;height:64px;border:1px solid var(--line);display:flex;align-items:center;justify-content:center;font-size:11px;font-weight:700;color:var(--green-dark)}
.who{position:absolute;top:1208px;left:0;width:1200px;height:552px;background:var(--green-band);color:#fff;text-align:center;padding-top:70px;overflow:hidden}
.who h2{font-size:54px;font-weight:800;letter-spacing:2px}
.who p{width:460px;margin:20px auto 0;font-size:13px;line-height:1.5}
.who .btn{display:inline-block;margin-top:22px;border:1px solid #fff;padding:7px 20px;font-size:11px;font-weight:600}
.laptop{width:560px;height:240px;margin:34px auto 0;border:12px solid #333;border-bottom:0;border-radius:10px 10px 0 0;background:linear-gradient(180deg,#ffffff 0%,#f4f7f4 40%,#dbe8d8 75%,#b9d3b3 100%)}
.testimonials{position:absolute;top:1806px;left:0;width:1200px;text-align:center}
.testimonials h2{font-family:"Raleway",sans-serif;font-weight:300;font-size:54px;letter-spacing:6px;color:#444}
.quotes{display:flex;justify-content:center;gap:30px;margin-top:28px}
.quote{width:410px;height:220px;border:1px solid var(--line);padding:20px;text-align:left;font-size:11px;color:#666;line-height:1.5}
.quote-head{display:flex;gap:12px;align-items:center;margin-bottom:12px}
.avatar{width:46px;height:46px;border-radius:50%;background:#c9c3bd}
.quote-head b{display:block;color:#333;font-size:11px}
.stars{color:#f2b01e;font-size:13px}
.dots{display:flex;justify-content:center;gap:8px;margin-top:22px}
.dots i{width:10px;height:10px;border-radius:50%;background:#ccc}
.dots i.on{background:#444}
.footer{position:absolute;top:2160px;left:0;width:1200px;height:224px;background:var(--footer);padding:26px 170px 0;display:flex;gap:50px;font-size:10px;color:#666}
.fcol h4{font-size:11px;color:#333;margin-bottom:6px}
.fcol div{line-height:1.7}
.fabout{margin-left:auto;width:330px;line-height:1.5}
.fabout .brand{color:var(--green-dark);font-size:13px;width:auto;margin-bottom:6px}
.fabout .brand-mark{background:var(--green-dark);width:12px;height:12px}
.pay{display:flex;gap:6px;margin-top:10px}
.pay i{width:34px;height:20px;background:#d0d0d0;border-radius:3px}
.social{display:flex;gap:6px;margin-top:10px}
.social i{width:18px;height:18px;border-radius:50%;background:var(--green)}
.copy{position:absolute;bottom:14px;left:170px;font-size:9px;color:#888}
</style>
</head>
<body>
<div class="topbar"><span>Welcome to Ledger Forms Depot</span><span>Login | My Account | Cart (0)</span></div>
<header class="header">
  <div class="brand"><span class="brand-mark"></span>ShopLedgerForms</div>
  <form class="search"><input value="Search by product name"><button type="button"><svg width="14" height="14" viewBox="0 0 14 14"><circle cx="6" cy="6" r="4.5" fill="none" stroke="#fff" stroke-width="2"/><line x1="9.5" y1="9.5" x2="13" y2="13" stroke="#fff" stroke-width="2"/></svg></button></form>
  <div class="shipping"><svg width="30" height="20" viewBox="0 0 30 20"><rect x="1" y="3" width="17" height="11" fill="#fff"/><path d="M18 6h6l4 4v4H18z" fill="#fff"/><circle cx="7" cy="16" r="3" fill="#fff" stroke="#1e6a18" stroke-width="1.5"/><circle cx="23" cy="16" r="3" fill="#fff" stroke="#1e6a18" stroke-width="1.5"/></svg>Fast Shipping</div>
</header>
<nav class="nav"><a>Business Checks</a><a>Computer Checks</a><a>Deposit Slips</a><a>Accessories</a><a>Help Desk</a><a>Reorder</a></nav>

<section class="hero">
  <div class="hero-col">
    <h2>Computer Checks</h2>
    <ul><li>100% software compatible</li><li>Bank-safe ink</li><li>Free ship</li></ul>
    <span class="hero-btn">Shop Now</span>
    <div class="check-art computer" role="img" aria-label="Fanned stack of computer check sheets in pink, green and blue"></div>
  </div>
  <div class="hero-col">
    <h2>Manual Checks</h2>
    <ul><li>Fits all 7 ring binders</li><li>Bank-safe ink</li><li>Free ship</li></ul>
    <span class="hero-btn">Shop Now</span>
    <div class="check-art manual" role="img" aria-label="Open binder of manual checks in lilac, blue and green"></div>
  </div>
</section>

<section class="categories">
  <div class="card"><h3>TallyBooks Checks</h3><div class="card-img" role="img" aria-label="TallyBooks compatible checks" style="background:linear-gradient(135deg,#e7f2e4,#b9dcae)"></div><span class="tag">Special Offer – Free Logo – Order</span><p>Laser checks made to work with your books. Fast print and ship.</p><p class="price">From $39.95</p></div>
  <div class="card"><h3>Laser Checks</h3><div class="card-img" role="img" aria-label="Laser printed check sheets" style="background:linear-gradient(135deg,#f6d0cb,#e39a90)"></div><span class="tag">Low Cost – Free Sign – Nothing</span><p>Top, middle and bottom layouts. Secure paper in many colours.</p><p class="price">From $29.95</p></div>
  <div class="card"><h3>Deposit Slips</h3><div class="card-img" role="img" aria-label="Deposit slip books" style="background:linear-gradient(135deg,#e4eef8,#a9c6e6)"></div><span class="tag">Manual &amp; Computer Deposit Slips</span><p>Slips to match your checks for quick and clean bank runs.</p><p class="price">From $19.95</p></div>
  <div class="card"><h3>Check Accessories</h3><div class="card-img" role="img" aria-label="Check binders, stamps and envelopes" style="background:linear-gradient(135deg,#eeeeee,#bdbdbd)"></div><span class="tag">Envelopes, Stamps – Accessories</span><p>Binders, window envelopes and stamps for your office needs.</p><p class="price">From $9.95</p></div>
</section>

<h2 class="section-title">Checks <span>By layout</span></h2>
<div class="row">
  <div class="layout-ico"><i></i><i class="alt"></i><i class="alt"></i></div>
  <div class="layout-ico"><i class="alt"></i><i></i><i class="alt"></i></div>
  <div class="layout-ico"><i class="alt"></i><i class="alt"></i><i></i></div>
  <div class="layout-ico"><i></i><i></i><i class="alt"></i></div>
  <div class="layout-ico"><i></i><i></i><i></i></div>
  <div class="layout-ico"><i class="alt"></i><i></i><i></i></div>
  <div class="layout-ico"><i></i><i class="alt"></i><i></i></div>
  <div class="layout-ico"><i class="alt"></i><i></i><i class="alt"></i></div>
  <div class="layout-ico"><i></i><i class="alt"></i><i class="alt"></i></div>
</div>

<h2 class="section-title">Checks <span>By Software</span></h2>
<div class="row">
  <div class="soft">Finwise</div><div class="soft">Ledgerly</div><div class="soft">TallyBooks</div><div class="soft">Birchline</div><div class="soft">Sorrel</div><div class="soft">Paylo</div><div class="soft">CountPoint</div><div class="soft">Acctly</div><div class="soft">Numera</div>
</div>

<section class="who">
  <h2>WHO WE ARE</h2>
  <p>We are a trusted check supplier for small and medium companies. 100% of our blank computer checks and check stock are compatible. 100% of our blank computer checks are bank approved.</p>
  <span class="btn">LEARN MORE</span>
  <div class="laptop" role="img" aria-label="Laptop showing the online check store with its green header and product table"></div>
</section>

<section class="testimonials">
  <h2>TESTIMONIALS</h2>
  <div class="quotes">
    <div class="quote"><div class="quote-head"><div class="avatar" role="img" aria-label="Customer portrait"></div><div><b>MARA, RIVERTON, OR</b><span class="stars">★★★★★</span></div></div>
    <p>A great place to shop for business checks and envelopes. Everything arrived on time, the checks printed cleanly and the price was fair. Ordering was easy and the support team answered every question fast. I will reorder from here for all of our office check needs without a doubt.</p></div>
    <div class="quote"><div class="quote-head"><div class="avatar" role="img" aria-label="Customer portrait"></div><div><b>DALTON, PINECREST, GA</b><span class="stars">★★★★★</span></div></div>
    <p>Good company that was able to deliver the checks to me quickly at a fair price. They were able to match my software in no time at all. The checks looked just right and the team kept me informed the whole way. Thank you for the great care.</p></div>
  </div>
  <div class="dots"><i class="on"></i><i></i></div>
</section>

<footer class="footer">
  <div class="fcol"><h4>How to Order</h4><div>Checks<br>Reorder<br>Order Status<br>Returns</div></div>
  <div class="fcol"><h4>Info</h4><div>About Us<br>Privacy<br>Terms<br>FAQ</div></div>
  <div class="fcol"><h4>Support</h4><div>Contact<br>Shipping Info<br>Bank Safety<br>Help Desk</div></div>
  <div class="fcol"><h4>Information</h4><div>Gift Cards<br>Coupons<br>Samples<br>Site Map</div><div class="social"><i></i><i></i><i></i></div></div>
  <div class="fabout"><div class="brand"><span class="brand-mark"></span>ShopLedgerForms</div>Ledger Forms Depot is your trusted source for quality business checks, deposit slips and office supplies. We print with secure paper and ship fast to every state at a fair price.<div class="pay"><i></i><i></i><i></i><i></i></div></div>
  <div class="copy">Copyright © Ledger Forms Depot. All rights reserved.</div>
</footer>
</body>
</html>
```